Window Advertisment for Rentals Company

I own a property rental company in Cyprus and I am looking for an eye catching design to place in my window to attract passers by.

Please check the attachment for more details.

Ad size to be 309cm x 204cm landscape

The font of the logo is velocity

Target Market(s)

Property Owners

Industry/Entity Type

It Company

Requirements
Must have
• The colours from my logo and be eye catching and make passers by take notice

```html
<!DOCTYPE html>
<html lang="en">
<head>
<meta charset="utf-8">
<title>Harbour Stays Cyprus – Window Advertisement</title>
<link href="https://fonts.googleapis.com/css2?family=Comfortaa:wght@700&family=Oswald:wght@300;600;700&family=Patrick+Hand+SC&display=swap" rel="stylesheet">
<style>
  :root {
    --frame: #000000;
    --orange: #f07828;
    --yellow: #fdc416;
    --brown: #6b2a0c;
    --white: #ffffff;
    --outline: #3a1a08;
  }
  * { box-sizing: border-box; margin: 0; padding: 0; }
  html, body { width: 1200px; height: 800px; overflow: hidden; background: var(--frame); }
  .poster { position: relative; width: 1200px; height: 800px; background: var(--frame); }
  .panel { position: absolute; left: 24px; top: 16px; width: 1156px; height: 764px; background: var(--yellow); overflow: hidden; }

  .headline {
    position: absolute; left: 0; top: 0; width: 1156px; height: 144px;
    background: var(--orange);
    display: flex; flex-direction: column; justify-content: center; align-items: center;
    font-family: "Comfortaa", sans-serif; font-weight: 700; font-size: 43px;
    color: var(--white); letter-spacing: 1.5px; word-spacing: 8px; line-height: 54px;
    text-shadow: 2px 2px 0 var(--outline), -1px -1px 0 var(--outline), 1px -1px 0 var(--outline), -1px 1px 0 var(--outline);
  }

  .hero {
    position: absolute; left: 0; top: 154px; width: 1156px; height: 306px;
    background: linear-gradient(180deg, #d6dade 0%, #c9c7c0 40%, #8fae73 60%, #e9d8c4 78%, #efdecb 100%);
  }
  .hero-tagline {
    position: absolute; left: 266px; top: 374px;
    font-family: "Patrick Hand SC", cursive; font-size: 32px; line-height: 36px;
    color: var(--brown); letter-spacing: 0.5px;
  }
  .reach-pill {
    position: absolute; left: 34px; top: 410px; width: 740px; height: 50px;
    background: var(--yellow); border-radius: 26px 26px 0 0;
    display: flex; align-items: center; justify-content: center;
    font-family: "Oswald", sans-serif; font-weight: 700; font-size: 32px;
    color: var(--brown);
  }

  .gallery { position: absolute; top: 470px; height: 208px; }
  .gallery.villa { left: 0; width: 274px; background: linear-gradient(180deg, #e8e6e0 0%, #e4ddd2 55%, #5fc0e6 100%); }
  .gallery.bedroom { left: 278px; width: 286px; background: linear-gradient(180deg, #f1f1f1 0%, #e6e3de 70%, #b89a7c 100%); }
  .gallery.lounge { left: 568px; width: 258px; background: linear-gradient(180deg, #eeefee 0%, #dfe2e2 65%, #cfcbc5 100%); }

  .brand-box { position: absolute; left: 832px; top: 470px; width: 324px; height: 208px; background: var(--white); overflow: hidden; }
  .brand-dot { position: absolute; left: 20px; top: 66px; width: 16px; height: 16px; border-radius: 50%; background: var(--yellow); }
  .brand-name {
    position: absolute; left: 44px; top: 56px; width: 260px;
    font-family: "Comfortaa", sans-serif; font-weight: 700; font-size: 31px; line-height: 34px;
    color: var(--orange);
  }
  .call-arc { position: absolute; left: 0; top: 142px; width: 324px; height: 66px; }
  .call-text {
    position: absolute; left: 0; top: 164px; width: 324px; text-align: center;
    font-family: "Oswald", sans-serif; color: var(--white); line-height: 40px;
  }
  .call-text .label { font-weight: 300; font-size: 24px; }
  .call-text .number { font-weight: 700; font-size: 30px; }

  .benefit {
    position: absolute; top: 696px; height: 68px;
    background: var(--orange); border-radius: 32px 32px 0 0;
    display: flex; align-items: center; justify-content: center; padding-top: 8px;
    font-family: "Oswald", sans-serif; font-weight: 600; font-size: 19px;
    color: var(--white); letter-spacing: 0.6px;
    text-shadow: 1px 1px 1px rgba(60,20,0,.6);
  }
  .benefit.commissions { left: 26px; width: 184px; }
  .benefit.payouts { left: 220px; width: 158px; }
  .benefit.advertising { left: 389px; width: 186px; }

  .web-address {
    position: absolute; left: 600px; top: 708px; width: 556px; text-align: center;
    font-family: "Comfortaa", sans-serif; font-weight: 700; font-size: 32px;
    color: var(--brown); letter-spacing: 0.5px;
  }
</style>
</head>
<body>
<div class="poster">
  <div class="panel">
    <header class="headline">
      <span>we are looking for villas and apartments</span>
      <span>to fulfill our growing demand of rentals</span>
    </header>

    <div class="hero" role="img" aria-label="Beachfront modern villas with lawns and families playing on the sand"></div>
    <p class="hero-tagline">CONNECT WITH OVER 35 LEADING WEBSITES</p>
    <p class="reach-pill">BE SEEN BY 100+ MILLION TRAVELLERS PER MONTH</p>

    <div class="gallery villa" role="img" aria-label="White villa with a blue swimming pool and sun loungers"></div>
    <div class="gallery bedroom" role="img" aria-label="Bright apartment with dining table, sofa and bed"></div>
    <div class="gallery lounge" role="img" aria-label="Living room with leather sofa, blue rug and patio doors"></div>

    <div class="brand-box">
      <span class="brand-dot"></span>
      <p class="brand-name">harbour stays cyprus</p>
      <svg class="call-arc" viewBox="0 0 324 66" preserveAspectRatio="none" aria-hidden="true">
        <path d="M0 66 C40 10 110 0 162 0 C214 0 284 10 324 66 Z" fill="var(--orange)"/>
      </svg>
      <p class="call-text"><span class="label">Call us: </span><span class="number">24 555180</span></p>
    </div>

    <div class="benefit commissions">LOW COMMISSIONS</div>
    <div class="benefit payouts">QUICK PAYOUTS</div>
    <div class="benefit advertising">FREE ADVERTISING</div>

    <p class="web-address">www.harbourstayscyprus.com</p>
  </div>
</div>
</body>
</html>
```